TLM #4319 - Homepage Design

Theme: Sophisticated yet sporty and easy to navigate
Accent Color: Green to match the logo - if something else looks better with the design, then go for it.
Background: A curvy road possibly with a high end Italian car on it or a race track
Content Background: Can't exceed 950 pix wide. If there is an image in the background, then it may be best to make it somewhat transparent so you can see the image.

Banner:
Logo Attached
Phone: 214-555-0183
Address: 4871 Pinecrest Ave. #200
Carrollton, TX 75098
Include social buttons in the banner: Chatterbook, Chirpline, Viewtube, Blog & bidMart

Find 8 images of high end Italian vehicles & Valtero and use it in a slideshow
The images will include text such as: 'Buy with Confidence'

Include a space for a video as well

Make sure it says somewhere on the homepage: 'Been in business since 2004'

Large call to Action Buttons:
- Inventory
- Service
- Project Cars
- Contact Us

Requirements
Nice to have
• Dark background, but it may not work with the logo. If possible they would prefer a dark background.
Should not have
• No city backgrounds

```html
<!DOCTYPE html>
<html lang="en">
<head>
<meta charset="utf-8">
<title>TLM Performance – Home</title>
<link rel="stylesheet" href="https://fonts.googleapis.com/css2?family=Arimo:wght@400;700&display=swap">
<style>
:root{
  --green:#0f8a3c;
  --green-dark:#0b6e2f;
  --ink:#222;
  --muted:#6f6f6f;
  --light:#ececec;
  --footer:#333333;
  --white:#ffffff;
}
*{box-sizing:border-box;margin:0;padding:0}
html,body{width:1110px;height:1200px;overflow:hidden}
body{font-family:"Arimo",Arial,sans-serif;color:var(--ink);background:var(--light);position:relative}

/* Header */
.hero{position:absolute;left:0;top:0;width:1110px;height:494px;
  background:radial-gradient(ellipse at 50% 60%,#5a5a5a 0%,#2b2b2b 50%,#0d0d0d 100%)}
.main-nav{position:absolute;left:230px;top:22px;width:138px;height:144px;
  background:linear-gradient(#ffffff,#e3e3e3);border-radius:5px;
  box-shadow:0 4px 10px rgba(0,0,0,.6);padding:20px 20px 0 21px;z-index:2}
.main-nav a{display:block;font-size:11px;font-variant:small-caps;color:var(--green);
  text-decoration:none;height:22px;line-height:16px;border-bottom:1px solid #dcdcdc;white-space:nowrap}
.main-nav a:last-child{border-bottom:0}
.main-nav a.is-current{color:var(--ink)}
.brand{position:absolute;left:380px;top:58px;height:48px;display:flex;align-items:center;gap:12px;white-space:nowrap}
.brand-mark{width:40px;height:40px;background:var(--green);flex:none}
.brand-name{font-size:34px;line-height:40px;font-weight:700;color:var(--green);letter-spacing:1px;white-space:nowrap}
.tagline{position:absolute;left:546px;top:114px;font-size:18px;line-height:22px;color:var(--white);font-variant:small-caps;letter-spacing:.5px;white-space:nowrap}

.slider{position:absolute;left:194px;top:155px;width:666px;height:311px;
  background:linear-gradient(180deg,#eef1f3 0%,#c9cfd4 28%,#6d6452 55%,#7e7d7a 75%,#454545 100%)}
.slider-guide{position:absolute;left:40px;top:48px;width:1px;height:245px;background:rgba(255,255,255,.35)}
.slider-base{position:absolute;left:40px;top:285px;width:510px;height:1px;background:rgba(255,255,255,.3)}
.slide-caption{position:absolute;left:26px;top:163px;width:224px;height:37px;white-space:nowrap;
  background:rgba(70,70,70,.8);color:var(--white);font-size:21px;line-height:37px;padding-left:24px}
.slider-dots{position:absolute;left:46px;top:288px;display:flex;gap:3px}
.slider-dots span{width:7px;height:7px;background:#9a9a9a}
.slider-dots span.is-active{background:#222}
.social{position:absolute;left:563px;top:273px;display:flex;gap:6px}
.social a{width:17px;height:17px;border-radius:50%;background:var(--green-dark);border:1px solid #6fbf88;display:block}

/* Intro section */
.feature{position:absolute;left:0;top:494px;width:1110px;height:262px;
  background:linear-gradient(90deg,#e4e4e4,#f6f6f6 40%,#efefef)}
.video{position:absolute;left:194px;top:57px;width:267px;height:150px;background:#0a0a0a;padding:6px}
.video-frame{width:255px;height:116px;background:linear-gradient(180deg,#8fa3a0,#c9cfcd 50%,#58605c)}
.video-play{position:absolute;left:114px;top:45px;width:44px;height:44px;border-radius:50%;background:rgba(60,60,60,.75)}
.video-bar{position:absolute;left:6px;bottom:6px;right:6px;height:20px;display:flex;align-items:center;gap:8px;padding:0 8px}
.video-bar .track{flex:1;height:5px;border:1px solid #666}
.video-bar .hd{font-size:8px;font-weight:700;color:#3ab0e0}
.feature-copy{position:absolute;left:503px;top:55px;width:358px}
.feature-copy h1{font-size:17px;font-weight:400;color:var(--green);margin-bottom:17px;white-space:nowrap}
.feature-copy p{font-size:9px;line-height:11px;color:var(--muted);margin-bottom:10px}
.btn-video{position:absolute;left:0;top:137px;width:110px;height:22px;border:1px solid #b9d8c2;background:#fff;
  display:flex;align-items:center;gap:9px;padding-left:3px;font-size:10px;color:var(--green);text-decoration:none;white-space:nowrap}
.btn-video svg{flex:none}

/* Call to action */
.actions{position:absolute;left:0;top:756px;width:1110px;height:316px;
  background:linear-gradient(180deg,#dcdcdc,#e8e8e8 50%,#e0e0e0)}
.actions-intro{position:absolute;left:320px;top:48px;width:470px;text-align:center;font-size:11px;line-height:14px;color:var(--green)}
.cta{position:absolute;top:115px;width:157px;height:139px;background:var(--white);text-align:center;text-decoration:none;color:var(--green)}
.cta h2{font-size:13px;font-weight:700;margin-top:23px}
.cta .icon{width:44px;height:44px;border-radius:50%;background:var(--green);margin:12px auto 0;display:flex;align-items:center;justify-content:center}
.cta .more{display:block;font-size:10px;margin-top:16px}
.cta.is-active{background:var(--green);color:var(--white)}
.cta.is-active .icon{background:var(--white)}
.cta-inventory{left:192px}.cta-service{left:364px}.cta-projects{left:534px}.cta-contact{left:704px}

.spacer{position:absolute;left:0;top:1072px;width:1110px;height:50px;background:#f2f2f2}
.footer{position:absolute;left:0;top:1122px;width:1110px;height:78px;background:var(--footer);border-top:6px solid var(--green)}
.footer-brand{position:absolute;left:192px;top:38px;display:flex;align-items:center;gap:6px;white-space:nowrap}
.footer-brand .brand-mark{width:20px;height:20px}
.footer-brand .brand-name{font-size:19px;line-height:22px}
.copyright{position:absolute;left:438px;top:45px;font-size:8px;color:#9a9a9a;white-space:nowrap}
</style>
</head>
<body>

<header class="hero" role="img" aria-label="Black and white photo of a winding mountain road">
  <nav class="main-nav">
    <a class="is-current" href="#">Home</a>
    <a href="#">About Us</a>
    <a href="#">Services</a>
    <a href="#">Project Cars</a>
    <a href="#">Contact Us</a>
  </nav>
  <div class="brand"><span class="brand-mark"></span><span class="brand-name">TLM PERFORMANCE</span></div>
  <p class="tagline">Been in business since 2004</p>

  <section class="slider">
    <div class="slider-photo" role="img" aria-label="Dark Valtero sports car driving on a mountain road under sunbeams"></div>
    <span class="slider-guide"></span><span class="slider-base"></span>
    <p class="slide-caption">Buy with Confidence</p>
    <div class="slider-dots"><span></span><span></span><span></span><span></span><span></span><span></span><span class="is-active"></span><span></span></div>
    <div class="social">
      <a href="#" aria-label="Chatterbook"></a>
      <a href="#" aria-label="Chirpline"></a>
      <a href="#" aria-label="Viewtube"></a>
      <a href="#" aria-label="Blog"></a>
    </div>
  </section>
</header>

<section class="feature" role="img" aria-label="Faded photo of a red sports car speeding on a road">
  <div class="video">
    <div class="video-frame" role="img" aria-label="Video still of white sports cars driving in formation"></div>
    <span class="video-play"></span>
    <div class="video-bar">
      <svg width="10" height="10" viewBox="0 0 10 10"><path d="M2 1l7 4-7 4z" fill="#fff"/></svg>
      <span class="track"></span><span class="hd">HD</span>
    </div>
  </div>
  <div class="feature-copy">
    <h1>Lorem Ipsum is simply dummy text</h1>
    <p>Lorem Ipsum is simply dummy text of the printing and typesetting industry. Lorem Ipsum has been the industry's standard dummy text ever since the 1500s, when an unknown printer took a galley of type and scrambled it to make a type specimen book.</p>
    <p>Lorem Ipsum is simply dummy text of the printing and typesetting industry. Lorem Ipsum has been the industry's standard dummy text ever since the 1500s, when an unknown printer took a galley</p>
    <a class="btn-video" href="#">
      <svg width="18" height="18" viewBox="0 0 18 18"><circle cx="9" cy="9" r="9" fill="#0f8a3c"/><path d="M7 5l6 4-6 4z" fill="#fff"/></svg>
      WATCH VIDEO
    </a>
  </div>
</section>

<section class="actions">
  <p class="actions-intro">Lorem Ipsum is simply dummy text of the printing and typesetting industry. Lorem Ipsum has been the industry's standard dummy text ever since the 1500s</p>

  <a class="cta cta-inventory" href="#">
    <h2>Inventory</h2>
    <span class="icon"><svg width="16" height="16" viewBox="0 0 16 16" fill="#fff"><rect x="1" y="9" width="3" height="6"/><rect x="6" y="6" width="3" height="9"/><rect x="11" y="3" width="3" height="12"/></svg></span>
    <span class="more">Learn More ›</span>
  </a>
  <a class="cta cta-service is-active" href="#">
    <h2>Service</h2>
    <span class="icon"><svg width="18" height="18" viewBox="0 0 18 18" fill="none" stroke="#0f8a3c" stroke-width="2"><path d="M5 3v13M3 3h4M12 2v14M10 5h4"/></svg></span>
    <span class="more">Learn More ›</span>
  </a>
  <a class="cta cta-projects" href="#">
    <h2>Project Cars</h2>
    <span class="icon"><svg width="20" height="20" viewBox="0 0 20 20" fill="none" stroke="#fff" stroke-width="1.6"><circle cx="10" cy="10" r="8"/><path d="M10 5v5l-3 3"/></svg></span>
    <span class="more">Learn More ›</span>
  </a>
  <a class="cta cta-contact" href="#">
    <h2>Contact Us</h2>
    <span class="icon"><svg width="20" height="20" viewBox="0 0 20 20" fill="none" stroke="#fff" stroke-width="1.4"><circle cx="10" cy="10" r="8"/><ellipse cx="10" cy="10" rx="3.5" ry="8"/><path d="M2 10h16M3.5 6h13M3.5 14h13"/></svg></span>
    <span class="more">Learn More ›</span>
  </a>
</section>

<div class="spacer"></div>

<footer class="footer">
  <div class="footer-brand"><span class="brand-mark"></span><span class="brand-name">TLM PERFORMANCE</span></div>
  <p class="copyright">Copyright All Right Reserved 2014.</p>
</footer>

</body>
</html>
```